Postcard Design

We need a postcard design for our company, Larkmere Business Group. Our firm sources funding (money) solutions for existing small business owners and start-up who are seeking $50,000 to $250,000. We would like to see designs that feature the colors dark or navy blue and gold. (We are uploading our logo for color reference ONLY. We DO NOT want the logo to be a part of the design!) The final design should communicate that we are an established financial source for business owners who are looking for capital to borrow. The final design should also emphasize that we provide quick approval and fast turnaround.
Target Market(s)
Small business owners (less than 10 employees) as well as start-up companies.
Industry/Entity Type
Small Business
Look and feel

```html
<!DOCTYPE html>
<html lang="en">
<head>
<meta charset="utf-8">
<title>Larkmere Business Group Postcard</title>
<link href="https://fonts.googleapis.com/css2?family=Tinos&display=swap" rel="stylesheet">
<style>
  :root {
    --frame-outer: #0a1a3d;
    --frame-gap: #f6efd9;
    --frame-inner: #c9a03a;
    --field-navy: #10275c;
    --accent-gold: #d9ac44;
    --badge-gold: #e8c260;
    --text-light: #ffffff;
  }
  html, body {
    margin: 0;
    padding: 0;
    overflow: hidden;
    background: var(--frame-gap);
  }
  .postcard {
    position: relative;
    width: 1200px;
    height: 926px;
    overflow: hidden;
    background: var(--frame-gap);
    font-family: "Tinos", "Times New Roman", serif;
  }
  .frame {
    position: absolute;
    box-sizing: border-box;
  }
  .frame-outer {
    inset: 0;
    border: 9px solid var(--frame-outer);
  }
  .frame-inner {
    inset: 16px;
    border: 7px solid var(--frame-inner);
  }
  .field {
    position: absolute;
    left: 28px;
    top: 28px;
    right: 27px;
    bottom: 30px;
    background: var(--field-navy);
  }
  .column-badge {
    position: absolute;
    border-radius: 9px;
    background: var(--badge-gold);
  }
  .column-badge--left { left: 152px; top: 151px; width: 109px; height: 95px; }
  .column-badge--right { left: 938px; top: 149px; width: 109px; height: 100px; }
  .brand-name, .brand-suffix, .tagline, .benefit {
    position: absolute;
    margin: 0;
    line-height: 1;
    white-space: nowrap;
    font-weight: 400;
  }
  .brand-name {
    left: 0; right: 0;
    top: 118px;
    text-align: center;
    font-size: 152px;
    color: var(--accent-gold);
  }
  .brand-suffix {
    left: 0; right: 0;
    top: 284px;
    padding-left: 14px;
    text-align: center;
    font-size: 110px;
    color: var(--accent-gold);
  }
  .tagline {
    left: 118px;
    top: 404px;
    font-size: 54px;
    color: var(--text-light);
  }
  .benefits-box {
    position: absolute;
    left: 174px;
    top: 488px;
    width: 858px;
    height: 363px;
    box-sizing: border-box;
    border: 13px solid var(--accent-gold);
  }
  .benefit {
    left: 202px;
    font-size: 36px;
    color: var(--accent-gold);
  }
  .benefit--line1 { top: 534px; }
  .benefit--line2 { top: 582px; }
  .benefit--approval { top: 676px; }
  .benefit--turnaround { top: 768px; }
</style>
</head>
<body>
  <main class="postcard">
    <div class="frame frame-outer"></div>
    <div class="frame frame-inner"></div>
    <div class="field"></div>

    <div class="column-badge column-badge--left" role="img" aria-label="Gold classical column icon"></div>
    <div class="column-badge column-badge--right" role="img" aria-label="Gold classical column icon"></div>

    <h1 class="brand-name">Larkmere</h1>
    <p class="brand-suffix">Business Group</p>
    <p class="tagline">Funding Solutions for Small Business Owners</p>

    <div class="benefits-box"></div>
    <p class="benefit benefit--line1">Established financial source for small business owners</p>
    <p class="benefit benefit--line2">looking for capital to borrow</p>
    <p class="benefit benefit--approval">Quick approval</p>
    <p class="benefit benefit--turnaround">Fast turnaround</p>
  </main>
</body>
</html>
```